Animal Hospital Business Cards

Make a business card look like the attached example

*Use the same blue/black coloring
*Brisket Hollow Animal Hospital (instead of pet home rounds)
*Emergency Services (instead of tamsin creek clinic)
*House Calls (instead of open 7 days by appointment)
*Change address to 278 Brisket Hollow Rd Loveland, OH 45263
*Open 7 days a week (instead of emergency service)
*Add the website www.briskethollowanimalhospital.example

On the back...
*instead of the text outlined in red, just white
*instead of the light blue, try your best to make it just like the blue and black on the front side of the card
*Delete "designed and printed by 9 whiskers inc, www.pressfeline.example

Requirements
Must have
• look just like the attached example with requested edits/changes

```html
<!DOCTYPE html>
<html lang="en">
<head>
<meta charset="utf-8">
<title>Brisket Hollow Animal Hospital – Business Card</title>
<link rel="stylesheet" href="https://fonts.googleapis.com/css2?family=Libre+Baskerville:ital,wght@0,400;0,700;1,400&family=Oswald:wght@500;700&family=Open+Sans:wght@400;600&display=swap">
<style>
  :root {
    --teal: #1f6a80;
    --teal-dark: #17576a;
    --ink: #151515;
    --paper: #f7f7f5;
    --red: #b3202f;
    --slate: #6a7797;
    --rule: #9aa0ad;
    --stage: #e6e2db;
    --mon: #c9508a;
    --tue: #e8823a;
    --wed: #5a9bc0;
    --thu: #d0313b;
    --fri: #c8ba2a;
    --sat: #c0406a;
    --sun: #1f7a3a;
  }
  * { box-sizing: border-box; margin: 0; padding: 0; }
  html, body { width: 1200px; height: 768px; overflow: hidden; }
  body {
    background: var(--stage);
    display: flex;
    align-items: center;
    justify-content: center;
    gap: 40px;
  }
  .card {
    position: relative;
    width: 540px;
    height: 309px;
    background: var(--paper);
    border-radius: 16px;
    overflow: hidden;
    box-shadow: 0 6px 18px rgba(0,0,0,.18);
    color: var(--ink);
  }
  .card__bands { position: absolute; inset: 0; width: 100%; height: 100%; }

  /* front */
  .front__hospital {
    position: absolute; left: 22px; top: 11px;
    font: 700 25px/1 "Libre Baskerville", serif;
    color: #fff; letter-spacing: .3px;
  }
  .front__housecalls {
    position: absolute; right: 26px; top: 72px; text-align: center;
    font-family: "Oswald", sans-serif;
  }
  .front__housecalls strong { display: block; font-weight: 700; font-size: 19px; line-height: 1; }
  .front__housecalls span { display: block; font-weight: 500; font-size: 7.5px; letter-spacing: .4px; }
  .front__doctor {
    position: absolute; left: 0; right: 0; top: 102px; text-align: center;
    font: 700 21px/1 "Libre Baskerville", serif;
  }
  .front__mark {
    position: absolute; left: 254px; top: 132px; width: 32px; height: 32px;
    border-radius: 50%; background: #cfa9a9;
  }
  .front__species {
    position: absolute; left: 0; right: 0; top: 172px; text-align: center;
    font: 400 13px/1 "Libre Baskerville", serif;
  }
  .front__species .dot { color: var(--red); }
  .front__web {
    position: absolute; left: 0; right: 0; top: 191px; text-align: center;
    font: italic 400 12.5px/1 "Libre Baskerville", serif;
  }
  .front__phone {
    position: absolute; left: 0; right: 0; top: 209px; text-align: center;
    font: 700 28px/1 "Libre Baskerville", serif; color: var(--red);
  }
  .front__address {
    position: absolute; left: 22px; bottom: 40px;
    font: 500 7.5px/1 "Oswald", sans-serif; letter-spacing: .3px; text-transform: uppercase;
  }
  .front__emergency {
    position: absolute; left: 22px; bottom: 14px;
    font: 700 20px/1 "Oswald", sans-serif; text-transform: uppercase;
  }
  .front__open {
    position: absolute; right: 26px; bottom: 12px;
    font: 700 25px/1 "Libre Baskerville", serif; color: #fff;
  }

  /* back */
  .back__title {
    position: absolute; left: 30px; top: 14px; color: #fff;
    font-family: "Libre Baskerville", serif; font-weight: 700;
  }
  .back__title .heading { font-size: 26px; line-height: 1.15; }
  .back__title .doctor { font-size: 18px; line-height: 1.3; }
  .back__title .phone { font-size: 25px; line-height: 1.2; }
  .back__form {
    position: absolute; left: 30px; right: 30px;
    font: 400 13px/1 "Open Sans", sans-serif; color: #555;
    display: flex; align-items: flex-end; gap: 8px;
  }
  .back__form--for { top: 140px; }
  .back__form--date { top: 258px; }
  .blank { flex: 1; border-bottom: 1px solid var(--rule); height: 13px; }
  .back__days {
    position: absolute; left: 30px; right: 30px; top: 180px;
    display: flex; justify-content: space-between;
  }
  .bone {
    width: 60px; height: 34px; border-radius: 17px;
    display: flex; align-items: center; justify-content: center;
    font: 600 12px/1 "Open Sans", sans-serif; color: #fff;
  }
  .bone--mon { background: var(--mon); }
  .bone--tue { background: var(--tue); }
  .bone--wed { background: var(--wed); }
  .bone--thu { background: var(--thu); }
  .bone--fri { background: var(--fri); }
  .bone--sat { background: var(--sat); }
  .bone--sun { background: var(--sun); }
</style>
</head>
<body>

<section class="card card--front">
  <svg class="card__bands" viewBox="0 0 540 309" aria-hidden="true">
    <rect x="0" y="0" width="540" height="50" fill="var(--teal)"/>
    <polygon points="0,50 430,50 0,64" fill="var(--ink)"/>
    <polygon points="250,309 272,256 540,256 540,309" fill="var(--teal)"/>
    <polygon points="390,256 540,242 540,256" fill="var(--ink)"/>
  </svg>
  <h1 class="front__hospital">Brisket Hollow Animal Hospital</h1>
  <div class="front__housecalls"><strong>HOUSE CALLS</strong><span>30 YEARS OF EXPERIENCE</span></div>
  <p class="front__doctor">Harlan J. Pettibone, DVM</p>
  <div class="front__mark" role="img" aria-label="Clinic emblem"></div>
  <p class="front__species">Cats <span class="dot">•</span> Dogs <span class="dot">•</span> Birds <span class="dot">•</span> Exotics</p>
  <p class="front__web">www.briskethollowanimalhospital.example</p>
  <p class="front__phone">(513) 555-0147</p>
  <p class="front__address">278 Brisket Hollow Rd. Loveland, OH 45263</p>
  <p class="front__emergency">Emergency Services</p>
  <p class="front__open">Open 7 days a week</p>
</section>

<section class="card card--back">
  <svg class="card__bands" viewBox="0 0 540 309" aria-hidden="true">
    <rect x="0" y="0" width="540" height="118" fill="var(--slate)"/>
  </svg>
  <div class="back__title">
    <p class="heading">Veterinary Appointment</p>
    <p class="doctor">Harlan J. Pettibone, DVM</p>
    <p class="phone">(513) 555-0147</p>
  </div>
  <div class="back__form back__form--for"><span>Your appointment for</span><span class="blank"></span><span>is on</span></div>
  <div class="back__days">
    <span class="bone bone--mon">Mon</span>
    <span class="bone bone--tue">Tues</span>
    <span class="bone bone--wed">Wed</span>
    <span class="bone bone--thu">Thu</span>
    <span class="bone bone--fri">Fri</span>
    <span class="bone bone--sat">Sat</span>
    <span class="bone bone--sun">Sun</span>
  </div>
  <div class="back__form back__form--date"><span>Date</span><span class="blank"></span><span class="blank"></span><span>AM/PM</span></div>
</section>

</body>
</html>
```